IT Service Provider

We need a website which reflects the IT Services we can offer to small and mid-size companies. This reaches from LAN/WAN, Security, VoIP, WiFi, Storage, Penetration testing.and Support.

In addition to that, a Logo is needed and should be embedded in the website.

Company is registered in the UK under:
Kovilant Ltd
Company No. 05927318

Industry/Entity Type

Security

```html
<!DOCTYPE html>
<html lang="en">
<head>
<meta charset="utf-8">
<title>Kovilant – IT Services Provider</title>
<link rel="stylesheet" href="https://fonts.googleapis.com/css2?family=Raleway:wght@600;700;800&family=Open+Sans:wght@400;600;700&display=swap">
<style>
:root{
  --green:#7cab1f;
  --green-dark:#5f8a14;
  --green-light:#9acb2d;
  --ink:#222222;
  --ink-soft:#555555;
  --header:#141414;
  --footer:#1a1a1a;
  --footer-text:#8a8a8a;
  --page:#f0f0f0;
  --card:#ffffff;
  --line:#e2e2e2;
}
*{box-sizing:border-box;margin:0;padding:0}
html,body{width:838px;height:1200px;overflow:hidden}
body{position:relative;background:var(--page);font-family:"Open Sans",Arial,sans-serif;color:var(--ink)}
.abs{position:absolute}

/* header */
.site-header{position:absolute;left:0;top:0;width:838px;height:102px;background:linear-gradient(#202020,var(--header))}
.brand{left:132px;top:34px;display:flex;align-items:center;gap:8px}
.brand-mark{width:16px;height:16px;background:var(--green)}
.brand-name{font-family:"Raleway",sans-serif;font-weight:800;font-size:28px;color:var(--green);letter-spacing:1px}
.account-links{right:120px;top:12px;display:flex;gap:30px}
.account-link{display:flex;gap:8px;align-items:flex-start;font-size:7px;line-height:9px;color:#ddd;white-space:nowrap}
.account-link b{display:block;color:var(--green);font-weight:600}
.lock{width:8px;height:10px;margin-top:1px}
.main-nav{left:517px;top:73px;display:flex;gap:13px;font-size:7.5px;color:#ddd;text-transform:uppercase;white-space:nowrap}
.main-nav .active{color:var(--green)}

/* hero */
.hero{left:0;top:102px;width:838px;height:290px;background:linear-gradient(100deg,#3a4350 0%,#1f2630 35%,#2c3340 60%,#6a7078 100%)}
.hero-caption{left:180px;top:230px;width:480px;text-align:center}
.hero-caption .rule{height:3px;background:var(--green)}
.hero-title{background:rgba(0,0,0,.82);color:#fff;font-family:"Raleway",sans-serif;font-weight:700;font-size:21px;letter-spacing:1.4px;text-align:center;padding:3px 0 1px;white-space:nowrap}
.hero-sub{display:inline-block;background:rgba(0,0,0,.82);color:#fff;font-size:12px;letter-spacing:.6px;text-align:center;padding:1px 14px 4px;white-space:nowrap}
.hero-dots{left:405px;top:368px;display:flex;gap:6px}
.hero-dots span{width:6px;height:6px;border-radius:50%;background:#fff}
.hero-dots .on{background:var(--green)}

/* newsletter */
.updates{left:0;top:392px;width:838px;height:86px;background:linear-gradient(var(--green-light),var(--green))}
.updates h2{position:absolute;top:8px;width:100%;text-align:center;font-family:"Raleway",sans-serif;font-weight:800;font-size:25px;color:#1b2a06;white-space:nowrap}
.field{position:absolute;top:48px;height:23px;background:#fff;font-size:8px;color:#999;padding:6px 10px;white-space:nowrap}
.subscribe{position:absolute;left:548px;top:48px;width:76px;height:23px;background:#222;color:#fff;font-size:8.5px;font-weight:700;text-align:center;line-height:23px}

/* packages */
.section-title{left:0;top:498px;width:838px;text-align:center;font-family:"Raleway",sans-serif;font-weight:800;font-size:44px;color:var(--ink)}
.title-rule{top:526px;height:1px;background:#d6d6d6;width:110px}
.package{top:578px;width:156px;height:268px;background:var(--card);border:1px solid var(--line);text-align:center}
.package .icon{position:absolute;left:56px;top:-22px;width:44px;height:44px;border-radius:50%;background:#fff;border:1px solid var(--line);display:flex;align-items:center;justify-content:center}
.package h3{position:absolute;top:32px;width:100%;font-size:14px;font-weight:700;color:#333}
.price{position:absolute;top:60px;left:0;width:100%;height:54px;border-top:1px solid var(--line);border-bottom:1px solid var(--line);display:flex;align-items:baseline;justify-content:center;padding-top:7px;color:#333}
.price .cur{font-size:22px;font-weight:700}
.price .amt{font-size:38px;font-weight:700;color:var(--green);line-height:38px}
.price .cents{font-size:17px;font-weight:600}
.price .per{font-size:14px;position:relative;top:-14px;margin-left:2px}
.features{position:absolute;top:128px;left:12px;width:130px;list-style:none;font-size:7.5px;color:#555;white-space:nowrap}
.features li{height:17px;line-height:17px;border-bottom:1px solid #ececec;margin:0 18px}
.features li:last-child{border-bottom:0}
.more{position:absolute;left:42px;top:232px;width:72px;height:23px;line-height:23px;background:var(--green);color:#fff;font-size:8.5px;font-weight:700}
.package.featured{background:linear-gradient(var(--green-light),var(--green-dark));border:0;top:576px;height:270px}
.package.featured .icon{background:#222;border:3px solid #fff;top:-20px}
.package.featured h3{color:#fff}
.package.featured .price{background:#222;color:#fff;border:0}
.package.featured .price .amt{color:#fff}
.package.featured .features{color:#fff;font-weight:700;top:126px}
.package.featured .features li{border-bottom:1px solid rgba(255,255,255,.7);margin:0 10px}
.package.featured .more{background:#222}
.package.wide-list .features li{margin:0 2px}

.panel{top:859px;height:121px;background:#fff;border:1px solid var(--line)}
.about{left:132px;width:422px;padding:10px 12px}
.about h4{font-size:14px;font-weight:700;color:#6a6a6a;margin-bottom:8px}
.about p{font-size:6.6px;line-height:9px;color:#666;margin-bottom:6px}
.about .read{font-size:6.6px;color:#888;margin-top:10px}
.payment{left:560px;width:156px;text-align:center;padding-top:14px}
.payment h4{font-size:15px;font-weight:700;color:#111;white-space:nowrap}
.payment h4 span{color:var(--green)}
.pay-name{margin-top:16px;font-size:22px;font-weight:700;color:#1f4a8f}
.cards{margin:8px auto 0;display:flex;gap:2px;width:100px;justify-content:center}
.cards i{display:block;width:23px;height:15px;border-radius:2px;background:#cfd6e0}

/* footer */
.footer-rule{left:0;top:992px;width:838px;height:8px;background:var(--green)}
.site-footer{left:0;top:1000px;width:838px;height:200px;background:var(--footer);color:var(--footer-text)}
.f-col{position:absolute;top:22px;font-size:6.6px;line-height:10px}
.f-col h5{font-family:"Open Sans",sans-serif;font-weight:400;font-size:13px;color:#fff;margin-bottom:8px;white-space:nowrap}
.f-col ul{list-style:none}
.f-col p+p{margin-top:10px}
.f-search{width:160px;height:16px;background:#fff;margin-top:22px;position:relative}
.f-search svg{position:absolute;right:6px;top:4px}
.f-divider{position:absolute;left:132px;top:135px;width:584px;height:1px;background:#2e2e2e}
.copyright{position:absolute;left:132px;top:155px;font-size:6.5px;line-height:10px;color:#ccc}
.social{position:absolute;left:600px;top:150px;display:flex;gap:10px}
.social span{width:10px;height:10px;border-radius:50%;background:#7a7a7a}
.social span.on{background:var(--green)}
</style>
</head>
<body>

<header class="site-header">
  <div class="abs brand"><span class="brand-mark"></span><span class="brand-name">Kovilant</span></div>
  <div class="abs account-links">
    <div class="account-link">
      <svg class="lock" viewBox="0 0 8 10"><path d="M2 4V3a2 2 0 014 0v1" stroke="#ddd" fill="none"/><rect x="0.5" y="4" width="7" height="5.5" fill="#ddd"/></svg>
      <div><b>CLIENT LOGIN</b>Create new account</div>
    </div>
    <div class="account-link">
      <svg class="lock" viewBox="0 0 8 10"><path d="M2 4V3a2 2 0 014 0v1" stroke="#ddd" fill="none"/><rect x="0.5" y="4" width="7" height="5.5" fill="#ddd"/></svg>
      <div><b>REGISTER NOW</b>Access your dashboard</div>
    </div>
  </div>
  <nav class="abs main-nav">
    <span class="active">Home</span><span>About us</span><span>Services</span><span>Packages</span><span>Contact us</span>
  </nav>
</header>

<section class="abs hero" role="img" aria-label="Photo of a hand touching a tablet with a glowing cloud and network device icons above it"></section>
<div class="abs hero-caption">
  <div class="rule"></div>
  <div class="hero-title">KOVILANT IT SERVICES PROVIDER</div>
  <div class="hero-sub">CALL US TODAY TO DISCUSS YOUR REQUIREMENT</div>
</div>
<div class="abs hero-dots"><span></span><span class="on"></span><span></span><span></span></div>

<section class="abs updates">
  <h2>FOR LATEST UPDATES FOR NEW PACKAGES</h2>
  <div class="field" style="left:214px;width:154px">Enter Your Name</div>
  <div class="field" style="left:382px;width:154px">Enter Your Email Address</div>
  <div class="subscribe">SUBSCRIBE</div>
</section>

<h2 class="abs section-title">PACKAGES</h2>
<div class="abs title-rule" style="left:190px"></div>
<div class="abs title-rule" style="left:538px"></div>

<article class="abs package" style="left:132px">
  <div class="icon"><svg width="20" height="14" viewBox="0 0 20 14"><path d="M5 13a4 4 0 010-8 5 5 0 019.5-1A4.5 4.5 0 0115 13z" fill="var(--green)"/></svg></div>
  <h3>Package 1</h3>
  <div class="price"><span class="cur">$</span><span class="amt">25</span><span class="cents">.69</span><span class="per">/mo</span></div>
  <ul class="features"><li>Kovilant Backup</li><li>Kovilant Storage</li><li>Kovilant Databases</li><li>Kovilant E-mail</li><li>Kovilant Servers</li><li>Kovilant Sites</li></ul>
  <div class="more">Learn More</div>
</article>

<article class="abs package featured" style="left:341px">
  <div class="icon"><svg width="20" height="20" viewBox="0 0 20 20" fill="none" stroke="#fff" stroke-width="1.5"><rect x="4" y="4" width="12" height="12"/><path d="M4 4l12 12M16 4L4 16"/></svg></div>
  <h3>Package 2</h3>
  <div class="price"><span class="cur">$</span><span class="amt">25</span><span class="cents">.69</span><span class="per">/mo</span></div>
  <ul class="features"><li>Managed Mobile Devices</li><li>Managed Networks</li><li>Managed Servers</li><li>Managed Workstations</li></ul>
  <div class="more">Learn More</div>
</article>

<article class="abs package wide-list" style="left:560px">
  <div class="icon"><svg width="20" height="20" viewBox="0 0 20 20"><path d="M8 10L15 4M8 10l7 6" stroke="var(--green)" stroke-width="1.5"/><circle cx="7" cy="10" r="4" fill="var(--green)"/><circle cx="15" cy="4" r="2.5" fill="var(--green)"/><circle cx="15" cy="16" r="2.5" fill="var(--green)"/></svg></div>
  <h3>Package 3</h3>
  <div class="price"><span class="cur">$</span><span class="amt">25</span><span class="cents">.69</span><span class="per">/mo</span></div>
  <ul class="features"><li>Contingency Planning</li><li>Platform Changes</li><li>Project Consulting</li><li>Relocations</li><li>Security &amp; Risk Management</li></ul>
  <div class="more">Learn More</div>
</article>

<section class="abs panel about">
  <h4>Who We Are</h4>
  <p>Contrary to popular belief, Lorem Ipsum is not simply random text. It has roots in a piece of classical Latin literature from 45 BC, making it over 2000 years old.</p>
  <p>Lorem Ipsum is simply dummy text of the printing and typesetting industry. Lorem Ipsum has been the industry's standard dummy text ever since the 1500s, when an unknown printer took a galley of type and scrambled it to make a type specimen book.</p>
  <div class="read">READ MORE &gt;&gt;</div>
</section>

<section class="abs panel payment">
  <h4>ONLINE <span>PAYMENT</span></h4>
  <div class="pay-name">PayNimbus</div>
  <div class="cards"><i></i><i></i><i></i><i></i></div>
</section>

<div class="abs footer-rule"></div>
<footer class="abs site-footer">
  <div class="f-col" style="left:132px;width:150px">
    <h5>Contact detail</h5>
    <p>Nunc tempus lorem vel augue, vitae semper eros. Integer facilisis, magna a porta tempor, velit nisi ultrices.</p>
    <p>Phone: 020 7946 0321<br>Fax: 020 7946 0322<br>Mail: hello@kovilant.example</p>
  </div>
  <div class="f-col" style="left:374px">
    <h5>Useful links</h5>
    <ul><li>Help and FAQs</li><li>Packages</li><li>Market View</li><li>Free Credit Report</li><li>Terms and Conditions</li><li>Privacy Policy</li><li>Community Guidelines</li></ul>
  </div>
  <div class="f-col" style="left:559px;width:165px">
    <h5>Don't miss out</h5>
    <p>Sed aliquam tellus quis dolor commodo, in porta magna facilisis. Donec rutrum, erat id varius congue, purus nibh cursus.</p>
    <div class="f-search"><svg width="5" height="7" viewBox="0 0 5 7"><path d="M1 0l4 3.5L1 7z" fill="#555"/></svg></div>
  </div>
  <div class="f-divider"></div>
  <div class="copyright">Copyright © 2014 KOVILANT.<br>All rights reserved.</div>
  <div class="social"><span></span><span class="on"></span><span></span><span></span><span></span><span></span></div>
</footer>

</body>
</html>
```